Foster/Adoptive Non Profit Needs Infographic of US and State of Montana Data

Infographic on 8 1/2 by 11 of US and Montana data. Sheet will be front and back and it will be printed on a high gloss stock as a leave behind to educate people of the need for fostering/adopting and supporting those who do. Even though it's about children, do not want it to look cartoonish or juvenile. Want it to be clean and easy to read. The front should include our logo. The front will be the data driven part of the infographic. The back will be mostly text, but should fit infographic style and flow. Files attached.

Target Market(s)

Churches, pastors, elder boards and child welfare partner organizations

Industry/Entity Type

Non Profit

Requirements
Must have
• Infographic look and feel
Should not have
• Even though this is about children, it should not be juvenile, or cartoonish.

```html
<!DOCTYPE html>
<html lang="en">
<head>
<meta charset="UTF-8">
<title>Kin Harbor – Foster/Adoptive Infographic</title>
<link href="https://fonts.googleapis.com/css2?family=Oswald:wght@400;500;700&family=Open+Sans:ital,wght@0,400;0,600;1,400&display=swap" rel="stylesheet">
<style>
  :root{
    --navy:#1d3a6b;
    --teal:#2aa3b8;
    --teal-dark:#1f8599;
    --orange:#f08a3c;
    --red:#e2483a;
    --coral:#f26b4f;
    --paper:#ffffff;
    --mist:#e8eef4;
    --map:#d6e0ea;
    --ink:#4a5563;
  }
  *{box-sizing:border-box;margin:0;padding:0}
  html,body{width:849px;height:1200px;overflow:hidden;background:var(--paper)}
  .sheet{position:relative;width:849px;height:1200px;background:var(--mist);font-family:'Open Sans',Arial,sans-serif;color:var(--ink);overflow:hidden}

  .masthead{position:absolute;left:0;top:0;width:849px;height:355px;background:var(--paper);text-align:center}
  .brand{position:absolute;top:26px;left:0;width:100%;text-align:center}
  .brand-row{display:inline-flex;align-items:center;gap:10px}
  .brand-dot{width:22px;height:22px;border-radius:50%;background:var(--teal)}
  .brand-name{font-family:'Oswald',sans-serif;font-weight:500;font-size:34px;line-height:1.2;color:var(--navy);letter-spacing:.5px}
  .brand-tag{font-size:10px;color:var(--navy);margin-top:2px;font-style:italic}
  .title-lead{position:absolute;top:170px;width:100%;font-family:'Oswald',sans-serif;font-weight:700;font-size:38px;line-height:1.1;color:var(--navy);letter-spacing:1px}
  .title-main{position:absolute;top:215px;width:100%;font-family:'Oswald',sans-serif;font-weight:700;font-size:70px;color:var(--teal);letter-spacing:1px;line-height:1}
  .title-sub{position:absolute;top:298px;width:100%;font-family:'Oswald',sans-serif;font-weight:700;font-size:30px;line-height:1.1;color:var(--navy);letter-spacing:.5px}

  .intro-band{position:absolute;left:0;top:365px;width:849px;height:82px;background:var(--teal);color:#fff;font-size:13.5px;line-height:1.45;font-style:italic;padding:12px 50px}

  .map-area{position:absolute;left:30px;top:460px;width:560px;height:300px;border-radius:40px 120px 80px 60px;background:var(--map);opacity:.7}

  .rally{position:absolute;left:40px;top:462px;font-family:'Oswald',sans-serif;font-weight:700;color:var(--orange);line-height:1}
  .rally .mid{font-size:42px}
  .rally .big{font-size:74px;color:var(--red);line-height:.98}

  .state-banner{position:absolute;left:580px;top:470px;width:269px;height:64px;background:var(--orange);clip-path:polygon(8% 0,100% 0,100% 100%,0 100%);color:#fff;font-family:'Oswald',sans-serif;font-weight:700;font-size:24px;line-height:1.1;padding:8px 0 0 40px;letter-spacing:.5px}
  .state-banner span{display:block;font-size:14px;font-weight:500;line-height:1.3;letter-spacing:1px}
  .state-facts{position:absolute;right:30px;top:550px;width:235px;text-align:right}

  .fact{margin-bottom:12px}
  .fact .num{font-family:'Oswald',sans-serif;font-weight:700;font-size:38px;line-height:1;color:var(--coral)}
  .fact .label{font-size:9.5px;font-weight:600;color:var(--ink);text-transform:uppercase;line-height:1.25;margin-top:3px}

  .nation-heading{position:absolute;left:40px;top:690px;font-family:'Oswald',sans-serif;font-weight:700;font-size:30px;color:var(--teal-dark);line-height:1}
  .nation-heading span{display:block;font-size:16px;font-weight:500;letter-spacing:1px;color:var(--navy);margin-top:2px}
  .nation-facts{position:absolute;left:40px;top:752px;width:185px}
  .nation-facts .fact{margin-bottom:12px}
  .nation-facts .num{font-size:30px;color:var(--navy)}

  .donut{position:absolute;left:240px;top:672px;width:320px;height:320px}

  .people{position:absolute;left:50px;top:1008px;width:749px;height:120px;border-radius:12px 12px 0 0;background:linear-gradient(90deg,#f26b4f,#f08a3c 30%,#2aa3b8 55%,#1d3a6b 78%,#e2483a)}
  .footer-band{position:absolute;left:0;bottom:0;width:849px;height:72px;background:var(--navy);color:#fff;text-align:center;font-size:15px;font-weight:600;padding-top:25px;letter-spacing:.2px}
</style>
</head>
<body>
<main class="sheet">
  <header class="masthead">
    <div class="brand">
      <div class="brand-row"><span class="brand-dot"></span><span class="brand-name">Kin Harbor</span></div>
      <div class="brand-tag">Bringing families and children together</div>
    </div>
    <h2 class="title-lead">WHY IS</h2>
    <h1 class="title-main">THE BODY OF CHRIST</h1>
    <h2 class="title-sub">NEEDED IN THE FOSTER/ADOPTIVE CRISIS?</h2>
  </header>

  <p class="intro-band">Foster care is a government run child welfare system that provides alternative living situations for children whose parents cannot offer protection or provision. Children in foster care may need these alternative supports temporarily, long term or permanently.</p>

  <div class="map-area" role="img" aria-label="Faint map of the United States with Montana highlighted"></div>

  <div class="rally">
    <div class="mid">WHO</div>
    <div class="big">CAN CHANGE</div>
    <div class="mid">THESE STAGGERING</div>
    <div class="mid">STATISTICS?</div>
  </div>

  <div class="state-banner">MONTANA<span>FOSTER CARE FACTS</span></div>
  <section class="state-facts">
    <div class="fact"><div class="num">223,982</div><div class="label">Children live in Montana</div></div>
    <div class="fact"><div class="num">2,600</div><div class="label">Montana children currently in foster care</div></div>
    <div class="fact"><div class="num">70,000</div><div class="label">Single parent Montana families exist</div></div>
    <div class="fact"><div class="num">11,000</div><div class="label">Montana children living with neither parent</div></div>
    <div class="fact"><div class="num">403</div><div class="label">Montana children waiting to be adopted</div></div>
    <div class="fact"><div class="num">8,000</div><div class="label">Montana children in care of their grandparents</div></div>
  </section>

  <div class="nation-heading">US<span>FOSTER CARE FACTS</span></div>
  <section class="nation-facts">
    <div class="fact"><div class="num">1 IN 184</div><div class="label">Children in the US are in the foster care system</div></div>
    <div class="fact"><div class="num">402,378</div><div class="label">Number of children living in the US foster care system</div></div>
    <div class="fact"><div class="num">101,840</div><div class="label">Are waiting for adoption</div></div>
    <div class="fact"><div class="num">74.2 MILLION</div><div class="label">Children live in the US</div></div>
  </section>

  <svg class="donut" viewBox="0 0 380 380" aria-label="Ring chart surrounding the word You">
    <g fill="none" transform="rotate(-90 190 190)">
      <circle cx="190" cy="190" r="172" stroke="#f7b38a" stroke-width="22" stroke-dasharray="700 381"/>
      <circle cx="190" cy="190" r="146" stroke="#f08a3c" stroke-width="22" stroke-dasharray="560 357"/>
      <circle cx="190" cy="190" r="120" stroke="#f26b4f" stroke-width="22" stroke-dasharray="620 134"/>
      <circle cx="190" cy="190" r="94" stroke="#e2483a" stroke-width="22" stroke-dasharray="430 161"/>
      <circle cx="190" cy="190" r="68" stroke="#c7362c" stroke-width="22" stroke-dasharray="360 68"/>
    </g>
    <circle cx="190" cy="190" r="54" fill="#ffffff"/>
    <text x="190" y="207" text-anchor="middle" font-family="Oswald, sans-serif" font-weight="700" font-size="48" fill="#e2483a">YOU</text>
  </svg>

  <div class="people" role="img" aria-label="Row of five stylised adults, each labelled You, representing church members who can help"></div>

  <footer class="footer-band">Empowering and Equipping the Church to Create a Foster/Adoptive Centric Culture of Prayer, Care and Support</footer>
</main>
</body>
</html>
```